New Advertising Company Business Card

A two sided business card. One side with logo only and the other side with my information and maybe my logo again. Looking for something unique and creative, but not too busy. Info would include my name(Marcus Feldon), President, phone number, address, email address, and website. LOGO IS THE BLUE AND WHITE ONE.

Target Market(s)

CEO/VP Level Audience

Industry/Entity Type

Business

Contact Information for Business Card

In Description.

```html
<!DOCTYPE html>
<html lang="en">
<head>
<meta charset="utf-8">
<title>Keystone Advertising – Business Card</title>
<link href="https://fonts.googleapis.com/css2?family=Open+Sans:wght@400;600;700&family=Roboto+Condensed:wght@400;700&display=swap" rel="stylesheet">
<style>
  :root {
    --brand-blue: #2570b8;
    --ink: #2a2a2c;
    --paper: #ffffff;
    --stage: #eceae6;
    --muted-white: #e9f1fa;
  }
  * { box-sizing: border-box; margin: 0; padding: 0; }
  html, body { width: 1200px; height: 1200px; overflow: hidden; }
  body {
    background: var(--stage);
    font-family: "Open Sans", sans-serif;
    position: relative;
  }
  .card {
    position: absolute;
    left: 150px;
    width: 900px;
    height: 514px;
    overflow: hidden;
    box-shadow: 0 6px 18px rgba(0,0,0,0.12);
  }
  .card--back { top: 60px; background: var(--brand-blue); }
  .card--front { top: 626px; background: var(--paper); }

  .wordmark {
    position: absolute;
    display: flex;
    align-items: center;
    gap: 18px;
    font-family: "Open Sans", sans-serif;
    font-weight: 700;
    letter-spacing: 0.06em;
    text-transform: uppercase;
    line-height: 1.05;
  }
  .wordmark__dot { width: 30px; height: 30px; border-radius: 50%; flex: none; }
  .card--back .wordmark {
    left: 50%; top: 50%;
    transform: translate(-50%, -50%);
    color: var(--paper);
    font-size: 52px;
  }
  .card--back .wordmark__dot { background: var(--paper); }
  .card--front .wordmark {
    left: 70px; top: 80px;
    color: var(--ink);
    font-size: 40px;
  }
  .card--front .wordmark__dot { background: var(--brand-blue); }

  .panels { position: absolute; inset: 0; }

  .identity {
    position: absolute;
    left: 665px; top: 120px;
    display: flex;
    align-items: center;
    gap: 14px;
    color: var(--paper);
  }
  .identity__name {
    font-family: "Roboto Condensed", sans-serif;
    font-weight: 700;
    font-size: 32px;
    line-height: 1.1;
  }
  .identity__title {
    font-family: "Roboto Condensed", sans-serif;
    font-size: 21px;
    line-height: 1.2;
  }

  .contact {
    position: absolute;
    left: 44px; top: 322px;
    list-style: none;
    color: var(--paper);
    font-size: 21px;
    line-height: 1.5;
  }
  .contact li { display: flex; align-items: center; gap: 12px; }
  .contact li.contact__cont { padding-left: 34px; }
  .contact svg { width: 22px; height: 22px; flex: none; }
</style>
</head>
<body>

  <section class="card card--back" aria-label="Card back">
    <div class="wordmark">
      <span class="wordmark__dot"></span>
      <span>Keystone<br>Advertising</span>
    </div>
  </section>

  <section class="card card--front" aria-label="Card front">
    <svg class="panels" width="900" height="514" viewBox="0 0 900 514" aria-hidden="true">
      <polygon points="640,0 870,0 870,250 690,250 660,272 632,250 632,0" fill="var(--ink)"/>
      <polygon points="0,292 612,292 648,264 672,264 690,252 870,252 870,514 0,514" fill="var(--brand-blue)"/>
      <line x1="612" y1="292" x2="648" y2="264" stroke="var(--paper)" stroke-width="3"/>
      <line x1="648" y1="264" x2="690" y2="252" stroke="var(--paper)" stroke-width="3"/>
    </svg>

    <div class="wordmark">
      <span class="wordmark__dot"></span>
      <span>Keystone<br>Advertising</span>
    </div>

    <div class="identity">
      <svg width="40" height="44" viewBox="0 0 40 44" aria-hidden="true">
        <circle cx="20" cy="13" r="11" fill="var(--paper)"/>
        <path d="M2 44 C2 30 10 26 20 26 C30 26 38 30 38 44 Z" fill="var(--paper)"/>
      </svg>
      <div>
        <p class="identity__name">Marcus Feldon</p>
        <p class="identity__title">President</p>
      </div>
    </div>

    <ul class="contact">
      <li>
        <svg viewBox="0 0 24 24" aria-hidden="true"><path d="M12 2a7 7 0 0 0-7 7c0 5 7 13 7 13s7-8 7-13a7 7 0 0 0-7-7zm0 9.5A2.5 2.5 0 1 1 12 6.5a2.5 2.5 0 0 1 0 5z" fill="var(--paper)"/></svg>
        <span>4170 Harbor Ridge Ave, Ste 210</span>
      </li>
      <li class="contact__cont"><span>Lakeview, CA 90410</span></li>
      <li>
        <svg viewBox="0 0 24 24" aria-hidden="true"><path d="M6.6 10.8a15 15 0 0 0 6.6 6.6l2.2-2.2a1 1 0 0 1 1-.25 11.4 11.4 0 0 0 3.6.57 1 1 0 0 1 1 1V20a1 1 0 0 1-1 1A17 17 0 0 1 3 4a1 1 0 0 1 1-1h3.5a1 1 0 0 1 1 1c0 1.25.2 2.45.57 3.6a1 1 0 0 1-.25 1z" fill="var(--paper)"/></svg>
        <span>555.214.7390</span>
      </li>
      <li>
        <svg viewBox="0 0 24 24" aria-hidden="true"><rect x="2" y="5" width="20" height="14" rx="1.5" fill="var(--paper)"/><path d="M3 6l9 7 9-7" fill="none" stroke="var(--brand-blue)" stroke-width="1.8"/></svg>
        <span>hello@keystonead.com</span>
      </li>
      <li>
        <svg viewBox="0 0 24 24" aria-hidden="true"><circle cx="12" cy="12" r="10" fill="var(--paper)"/><path d="M2 12h20M12 2c3 3 3 17 0 20M12 2c-3 3-3 17 0 20" fill="none" stroke="var(--brand-blue)" stroke-width="1.5"/></svg>
        <span>www.keystonead.com</span>
      </li>
    </ul>
  </section>

</body>
</html>
```